Plakat-Design für Online-Vertrieb von Messeständen an Unternehmen
Zielgruppe
Wir verkaufen über unseren Onlineshop (www.standhalle-beispiel.de) Messestände an Unternehmen.
Aufgabenstellung
Wir benötigten eine Grafik, die auf unseren Messeständen als Beispiel eingebunden werden kann. Sie soll unseren Kunden die Möglichkeit geben, dass sie sich das System besser vorstellen können. Da wir das System VORAQ nennen werden, befindet sich das dazugehörige Logo in der Anlage. Das Logo sollte auf dem Design sichtbar sein, aber muss nicht im Vordergrund stehen.
Das Messesystem ist variabel und in vielen verschiedenen Breiten und Formationen aufstellbar. Die Grafik muss bei Eckständen auch mal um die Ecke laufen. Somit wäre es perfekt, wenn die Grafik für verschiedene Breiten erweiterbar wäre. Die Standardhöhe des Systems liegt immer bei 2,5m.
Zwei Beispielvarianten mit blanko Grafik liegen in der Anlage und können gerne für die Visualisierung verwendet werden.
Gerne kann auch ein einfacher Farbverlauf mit modernen Farben verwendet werden. Wir sind hier aber sehr flexibel.
Die Messestände haben eine LED-Hinterleuchtung in ihren Motiven, sodass sie in Realität strahlend wirken.
Wenn wir ein Motiv finden würden, mit dem wir den 'Strahleffekt' gut visualisieren könnten, wäre das natürlich hervorragend.
Im folgenden finden Sie andere Beispiele von Messeständen inkl. Stoffgrafiken. Hier sieht man auch die variablen Standgrößen, welche eine Erweiterbarkeit des Motivs erforderlich machen.
Fast identisch zu unserem neuen System sind die Artikel in der Kategorie 'LED Messestand Stoff' (https://www.standhalle-beispiel.de/Messestand/LED-Messestand-Stoff/)
Ansonsten sind hier aber noch weitere Beispiele:
https://www.standhalle-beispiel.de/Messestand/Messestand-Stoff/
https://www.standhalle-beispiel.de/Messestand/LED-Messestand-Stoff/
https://www.standhalle-beispiel.de/Messebausysteme/TORVEK-NU/
https://www.standhalle-beispiel.de/Messebausysteme/Zorbin/Zorbin-ViewPanel/
https://www.standhalle-beispiel.de/Messebausysteme/Zorbin/Zorbin-WideCloth/

```html
<!DOCTYPE html>
<html lang="de">
<head>
<meta charset="utf-8">
<title>VORAQ Stoffgrafik</title>
<link href="https://fonts.googleapis.com/css2?family=Montserrat:wght@500&display=swap" rel="stylesheet">
<style>
  :root {
    --stage: #e9e6e2;
    --ink-deep: #0e0710;
    --ink-plum: #2a0f2e;
    --violet: #8a2fd0;
    --violet-soft: #5a1b8c;
    --amber: #f0a21a;
    --label: #ffffff;
  }
  * { margin: 0; padding: 0; box-sizing: border-box; }
  html, body {
    width: 1200px;
    height: 900px;
    overflow: hidden;
    background: var(--stage);
  }
  .fabric-graphic {
    position: absolute;
    left: 40px;
    top: 100px;
    width: 1120px;
    height: 700px;
    overflow: hidden;
    background:
      radial-gradient(ellipse at 70% 20%, var(--violet-soft) 0%, transparent 45%),
      radial-gradient(ellipse at 10% 90%, var(--violet-soft) 0%, transparent 40%),
      linear-gradient(135deg, var(--ink-plum) 0%, var(--ink-deep) 55%, var(--ink-plum) 100%);
  }
  .light-streaks {
    position: absolute;
    inset: 0;
    width: 100%;
    height: 100%;
  }
  .portrait-area {
    position: absolute;
    left: 270px;
    top: 90px;
    width: 390px;
    height: 560px;
    border-radius: 46% 46% 30% 30%;
    background:
      radial-gradient(ellipse at 55% 25%, rgba(230, 40, 80, 0.85) 0%, transparent 35%),
      radial-gradient(ellipse at 45% 40%, rgba(40, 160, 240, 0.8) 0%, transparent 35%),
      radial-gradient(ellipse at 60% 60%, rgba(245, 190, 30, 0.85) 0%, transparent 38%),
      radial-gradient(ellipse at 40% 75%, rgba(60, 40, 140, 0.9) 0%, transparent 55%);
    filter: blur(6px);
    opacity: 0.9;
  }
  .system-label {
    position: absolute;
    left: 790px;
    top: 96px;
    display: flex;
    align-items: center;
    gap: 14px;
    font-family: "Montserrat", "Helvetica Neue", sans-serif;
    font-weight: 500;
    font-size: 40px;
    letter-spacing: 6px;
    color: var(--label);
  }
  .system-label-square {
    width: 16px;
    height: 16px;
    background: var(--label);
  }
</style>
</head>
<body>
  <main class="fabric-graphic">
    <svg class="light-streaks" viewBox="0 0 1120 700" aria-hidden="true">
      <defs>
        <linearGradient id="streak-amber" x1="0" y1="1" x2="1" y2="0">
          <stop offset="0" stop-color="#f0a21a" stop-opacity="0"/>
          <stop offset="0.5" stop-color="#f0a21a" stop-opacity="0.85"/>
          <stop offset="1" stop-color="#f0a21a" stop-opacity="0"/>
        </linearGradient>
        <linearGradient id="streak-violet" x1="0" y1="1" x2="1" y2="0">
          <stop offset="0" stop-color="#8a2fd0" stop-opacity="0"/>
          <stop offset="0.5" stop-color="#b86cff" stop-opacity="0.9"/>
          <stop offset="1" stop-color="#8a2fd0" stop-opacity="0"/>
        </linearGradient>
      </defs>
      <g stroke-linecap="round">
        <line x1="0" y1="120" x2="330" y2="520" stroke="url(#streak-amber)" stroke-width="5"/>
        <line x1="40" y1="40" x2="420" y2="480" stroke="url(#streak-amber)" stroke-width="2"/>
        <line x1="400" y1="700" x2="900" y2="200" stroke="url(#streak-amber)" stroke-width="3"/>
        <line x1="520" y1="620" x2="1000" y2="120" stroke="url(#streak-amber)" stroke-width="6"/>
        <line x1="560" y1="0" x2="1120" y2="430" stroke="url(#streak-violet)" stroke-width="4"/>
        <line x1="700" y1="0" x2="1120" y2="330" stroke="url(#streak-violet)" stroke-width="2"/>
        <line x1="0" y1="560" x2="280" y2="700" stroke="url(#streak-violet)" stroke-width="5"/>
        <line x1="0" y1="480" x2="360" y2="700" stroke="url(#streak-violet)" stroke-width="2"/>
        <line x1="760" y1="700" x2="1120" y2="420" stroke="url(#streak-violet)" stroke-width="3"/>
      </g>
    </svg>
    <div class="portrait-area" role="img" aria-label="Porträt im Profil mit leuchtendem Neon-Farbpuder in Rot, Blau, Gelb und Violett"></div>
    <div class="system-label">
      <span class="system-label-square"></span>
      <span class="system-label-name">VORAQ</span>
    </div>
  </main>
</body>
</html>
```